依頼詳細
アルコール除菌ジェルのラベルのデザインをお願い致します
記載項目
サイズはW110mm×H154mm
ラミネート貼り
希望イメージ
シンプル 複雑
単色 カラフル
暗い 明るい
日常 高級
遊び心 厳粛
未来的 伝統的
女性的 男性的
希望する色
緑系
納品ファイル
• イラストレーター形式 (.ai)
補足説明
実際の現在のデザイン(他社)を添付致します。
添付のデザインのOEM製品になり弊社自社品となります
雰囲気を全然違うようにしてください
業務用です
添付の画像にありますQELTは必要ございません
また発売元は弊社で製造元は別な会社で記載頂くと思います
宜しくお願い致します
容器の画像を添付致しました。
円形のPETボトルになります
販売先は自動車ディーラー様中心となります

ディーラー様及び通常の販売先において頂けるデザインでした
関係者で3点選びましたが、全員がこの方のデザインが上がりましたので
決定しました

沢山の方からデザインをあげて頂き非常に迷いました。
今後もこのサイトを使って新商品のデザインや
容器のデザインをお願いしたいと思いますのでその際は
宜しいお願い致します。今回はありがとうございました

```html
<!DOCTYPE html>
<html lang="ja">
<head>
<meta charset="utf-8">
<title>アルコール除菌ジェル ラベル</title>
<link rel="stylesheet" href="https://fonts.googleapis.com/css2?family=Noto+Sans+JP:wght@400;500;700;900&family=Roboto:ital,wght@0,500;1,900&display=swap">
<style>
  :root{
    --bg:#ffffff;
    --label:#ffffff;
    --silver-light:#f4f5f7;
    --silver-mid:#c9ccd1;
    --silver-dark:#8f949b;
    --blue:#1f8fd6;
    --blue-deep:#0b5fa8;
    --blue-bright:#37b4ee;
    --ink:#222428;
    --ink-soft:#4a4d52;
    --red:#e0201c;
    --rule:#9a9da2;
  }
  *{box-sizing:border-box;margin:0;padding:0}
  html,body{width:1200px;height:1200px;overflow:hidden;background:var(--bg)}
  body{font-family:"Noto Sans JP",sans-serif;color:var(--ink)}
  .label{
    position:absolute;left:210px;top:54px;width:780px;height:1092px;
    background:var(--label);border-radius:26px;overflow:hidden;
    box-shadow:0 0 0 1px #e2e4e7;
  }
  .edge{position:absolute;left:0;width:100%;height:56px;
    background:linear-gradient(180deg,var(--silver-dark),var(--silver-light) 45%,var(--silver-mid))}
  .edge.top{top:0}
  .edge.bottom{bottom:0;transform:scaleY(-1)}
  .side{position:absolute;top:0;bottom:0;width:34px;
    background:linear-gradient(90deg,var(--silver-mid),rgba(255,255,255,0))}
  .side.left{left:0}
  .side.right{right:0;transform:scaleX(-1)}
  .headline{position:absolute;top:86px;left:0;width:100%;text-align:center;
    font-weight:900;font-style:italic;font-size:38px;color:var(--blue);letter-spacing:1px}
  .emblem{position:absolute;left:100px;top:150px;width:560px;height:380px}
  .emblem-text{position:absolute;left:100px;top:150px;width:560px;height:380px;text-align:center;color:#fff}
  .emblem-en{position:absolute;top:62px;left:0;width:100%;font-family:"Roboto",sans-serif;font-weight:500;font-size:24px;line-height:1.25}
  .emblem-ja{position:absolute;top:122px;left:0;width:100%;font-weight:900;font-size:78px;line-height:1.08;letter-spacing:2px}
  .emblem-sub{position:absolute;top:296px;left:0;width:100%;font-family:"Roboto",sans-serif;font-style:italic;font-weight:900;font-size:28px}
  .badge{position:absolute;left:612px;top:410px;width:112px;height:112px;border-radius:50%;
    background:#fff;border:4px solid var(--blue);display:flex;align-items:center;justify-content:center;
    text-align:center;font-weight:900;font-size:20px;line-height:1.2;color:var(--blue-deep)}
  .pill{position:absolute;left:235px;top:548px;width:340px;height:50px;border-radius:25px;
    background:linear-gradient(180deg,var(--blue-bright),var(--blue));color:#fff;
    font-weight:700;font-size:30px;text-align:center;line-height:50px;letter-spacing:2px}
  .volume{position:absolute;left:66px;top:585px;font-family:"Roboto",sans-serif;font-weight:500;font-size:46px}
  .category{position:absolute;left:0;width:100%;top:612px;text-align:center;font-weight:700;font-size:22px}
  .fire{position:absolute;left:580px;top:596px;width:130px;text-align:center}
  .fire-box{border:2px solid var(--red);color:var(--red);font-weight:900;font-size:22px;line-height:30px}
  .fire-note{font-size:13px;color:var(--ink-soft);margin-top:2px}
  .spec{position:absolute;left:60px;top:670px;width:660px;border-collapse:collapse;font-size:11px;line-height:1.45}
  .spec th,.spec td{border:1px solid var(--rule);padding:3px 6px;text-align:left;vertical-align:top;font-weight:400}
  .spec th{width:72px;background:#f1f2f4;letter-spacing:4px}
  .notes{position:absolute;left:60px;top:790px;width:660px;font-size:10.5px;line-height:1.5;color:var(--ink)}
  .notes h2{font-size:11px;font-weight:700;margin-top:4px}
  .makers{position:absolute;left:60px;top:986px;width:660px;display:flex;justify-content:space-between;
    border-top:1px solid var(--rule);padding-top:6px;font-size:10.5px;line-height:1.5}
  .makers b{font-weight:700;margin-right:6px}
</style>
</head>
<body>
<main class="label">
  <div class="edge top"></div>
  <div class="edge bottom"></div>
  <div class="side left"></div>
  <div class="side right"></div>

  <p class="headline">手指の細菌・ウイルスを消毒</p>

  <svg class="emblem" viewBox="0 0 560 380" aria-hidden="true">
    <defs>
      <linearGradient id="rim" x1="0" y1="0" x2="0" y2="1">
        <stop offset="0" stop-color="#ffffff"/>
        <stop offset=".35" stop-color="#b8bcc2"/>
        <stop offset=".6" stop-color="#6f747b"/>
        <stop offset="1" stop-color="#e9ebee"/>
      </linearGradient>
      <radialGradient id="face" cx=".45" cy=".35" r=".75">
        <stop offset="0" stop-color="#5cc8f5"/>
        <stop offset=".55" stop-color="#1f8fd6"/>
        <stop offset="1" stop-color="#0b4f95"/>
      </radialGradient>
    </defs>
    <ellipse cx="280" cy="190" rx="278" ry="188" fill="url(#rim)"/>
    <ellipse cx="280" cy="190" rx="256" ry="168" fill="url(#face)"/>
    <ellipse cx="280" cy="118" rx="220" ry="80" fill="#ffffff" opacity=".12"/>
  </svg>
  <div class="emblem-text">
    <p class="emblem-en">Alcohol<br>Sanitization Gel</p>
    <h1 class="emblem-ja">アルコール<br>除菌ジェル</h1>
    <p class="emblem-sub">HAND GEL</p>
  </div>

  <div class="badge">手に<br>刷り込む<br>だけ!</div>

  <div class="pill">速乾ハンドジェル</div>
  <div class="volume">1ℓ</div>
  <p class="category">指定医薬部外品</p>
  <div class="fire">
    <div class="fire-box">火気厳禁</div>
    <div class="fire-note">(エタノール含有)</div>
  </div>

  <table class="spec">
    <tr><th>品名</th><td>アルコール除菌ジェル</td><th>性状</th><td>無色のわずかに混濁した粘性の液である。</td></tr>
    <tr><th>成分</th><td>エタノール(C2H6O)72.0〜77.0vol%</td><th>用途</th><td>手指・皮膚の洗浄・消毒</td></tr>
    <tr><th>添加物</th><td>グリセリン、カルボキシビニルポリマー、トリエタノールアミン</td><th>使用方法</th><td>適量を手のひらにとり、手指全体に伸ばし、乾燥するまで塗り込んでください。</td></tr>
  </table>

  <div class="notes">
    <h2>用法容量に関する注意</h2>
    <p>●次の人は使用しないでください。(1)本剤でかぶれたことのある人 (2)傷や湿疹のある人。●小児に使用させる場合は保護者の指導監督のもとに使用してください。●目に入らないよう注意し、入った場合はすぐに水で洗い流し、異常がある場合は眼科医の診療を受けてください。●外用にのみ使用してください。●使用後は手を十分に乾燥させてください。</p>
    <h2>保管および取り扱い上の注意</h2>
    <p>●直射日光の当たらない涼しい所に保管してください。●小児の手の届かない所に保管してください。●他の容器に入れ替えないでください。●火気に近づけないでください。●床や家具、革製品などに付着すると変質・変色のおそれがあります。</p>
    <p>【貯蔵】気密容器、火気を避けて室温保存。</p>
  </div>

  <div class="makers">
    <p><b>販売元</b>株式会社ミドリ商会<br>〒100-0000 東京都千代田区青葉町4-12-8 TEL.03-0000-1234</p>
    <p><b>製造元</b>株式会社カゼノ化成<br>〒530-0000 大阪府大阪市北区若葉台3-7-21 TEL.06-0000-5678</p>
  </div>
</main>
</body>
</html>
```